Sunny Paths and joy Business card

I have a logo, but will like a business card design. Is for a travel agency in Mexico. We focus in family experiences.

I will liek some thing different and unique, from the traditional business card, something to get remmeber for.

Business card information:

Leandro T. Ocampo
leandro@sunnypathsjoy.example

Alameda 482, 3 piso
Col. Tlalpizco
Mexico, D.F. 07320

office: (55) 5000-0142
mobile: (55) 9000-0187

www.sunnypathsjoy.example
@sunnypjoy
blog: sunnypathsandjoy.blogsite.example
facebook: SunnyPathsAndJoy

```html
<!DOCTYPE html>
<html lang="en">
<head>
<meta charset="utf-8">
<title>Sunny Paths and joy – Business card</title>
<link href="https://fonts.googleapis.com/css2?family=Arimo:wght@400;700&display=swap" rel="stylesheet">
<style>
  :root {
    --stage: #2b2b2b;
    --card: #efefef;
    --card-edge: #e2e2e2;
    --brand-blue: #1f5bb3;
    --band-top: #2f63b8;
    --band-bottom: #1c4590;
    --stitch: #9fb7df;
    --sky: #bfe0f3;
    --white: #ffffff;
  }
  * { margin: 0; padding: 0; box-sizing: border-box; }
  html, body {
    width: 1200px; height: 900px; overflow: hidden;
    background: var(--stage);
    font-family: "Arimo", Arial, sans-serif;
  }
  .card {
    position: absolute; left: 258px; width: 628px; height: 384px;
    background: var(--card);
    border: 1px solid var(--card-edge);
    border-radius: 9px; overflow: hidden;
    box-shadow: 0 6px 16px rgba(0,0,0,.45);
  }
  .card--front { top: 48px; }
  .card--back { top: 462px; }

  .social-band {
    position: absolute; left: 0; right: 0; bottom: 0; height: 60px;
    background: linear-gradient(var(--band-top), var(--band-bottom));
    display: flex; align-items: center; justify-content: center;
    color: var(--white); font-size: 14px; gap: 10px;
  }
  .social-band::before {
    content: ""; position: absolute; left: 0; right: 0; top: 3px;
    border-top: 1px dashed var(--stitch);
  }
  .social-item { display: flex; align-items: center; gap: 6px; }
  .social-dot { width: 11px; height: 11px; border-radius: 50%; background: var(--white); }
  .social-sep { opacity: .9; }

  .brand-mark {
    position: absolute; display: flex; align-items: center; gap: 12px;
  }
  .brand-mark__circle {
    border-radius: 50%; background: var(--sky); flex: none;
  }
  .brand-mark__name {
    color: var(--brand-blue); font-weight: 700; line-height: 1.05;
  }
  .card--front .brand-mark { left: 34px; top: 70px; }
  .card--front .brand-mark__circle { width: 62px; height: 62px; }
  .card--front .brand-mark__name { font-size: 27px; width: 180px; }
  .card--back .brand-mark { left: 50%; top: 82px; transform: translateX(-50%); }
  .card--back .brand-mark__circle { width: 74px; height: 74px; }
  .card--back .brand-mark__name { font-size: 31px; width: 210px; }

  .contact { position: absolute; left: 342px; top: 84px; color: var(--brand-blue); }
  .contact__name { font-size: 19px; font-weight: 700; letter-spacing: .2px; }
  .contact__title { font-size: 16px; margin-top: 8px; }
  .contact__address { font-size: 13.5px; line-height: 19px; margin-top: 36px; }
  .contact__line { display: flex; align-items: center; gap: 8px; font-size: 14px; line-height: 19.5px; }
  .contact__line svg { width: 11px; height: 11px; flex: none; fill: var(--brand-blue); }
  .contact__line--big { font-size: 15.5px; }

  .back-web {
    position: absolute; left: 0; right: 0; top: 244px; text-align: center;
    color: var(--brand-blue); font-size: 21px;
  }
</style>
</head>
<body>

<section class="card card--front">
  <div class="brand-mark">
    <span class="brand-mark__circle"></span>
    <span class="brand-mark__name">Sunny Paths and joy</span>
  </div>

  <div class="contact">
    <p class="contact__name">LEANDRO T. OCAMPO</p>
    <p class="contact__title">Director Executive</p>
    <p class="contact__address">Alameda 482, 3 piso Col. Tlalpizco<br>Mexico, D.F. 07320</p>
    <p class="contact__line">
      <svg viewBox="0 0 12 12"><path d="M2.5 1 4.5 3 3.6 4.4C4.3 6 6 7.7 7.6 8.4L9 7.5 11 9.5 9.8 11C5.5 10.7 1.3 6.5 1 2.2Z"/></svg>
      (55) 5000-0142
    </p>
    <p class="contact__line">
      <svg viewBox="0 0 12 12"><path d="M3.5 0.5h5v11h-5zM4.5 1.5v7.5h3V1.5z"/></svg>
      (55) 9000-0187
    </p>
    <p class="contact__line contact__line--big">
      <svg viewBox="0 0 12 12"><path d="M0.5 2.5h11v7h-11zM1.5 3.3 6 6.6 10.5 3.3z"/></svg>
      leandro@sunnypathsjoy.example
    </p>
    <p class="contact__line">
      <svg viewBox="0 0 12 12"><circle cx="6" cy="6" r="5.5"/></svg>
      www.sunnypathsjoy.example
    </p>
  </div>

  <footer class="social-band">
    <span class="social-item"><span class="social-dot"></span>@sunnypjoy</span>
    <span class="social-sep">|</span>
    <span class="social-item"><span class="social-dot"></span>sunnypathsandjoy.blogsite.example</span>
    <span class="social-sep">|</span>
    <span class="social-item"><span class="social-dot"></span>SunnyPathsAndJoy</span>
  </footer>
</section>

<section class="card card--back">
  <div class="brand-mark">
    <span class="brand-mark__circle"></span>
    <span class="brand-mark__name">Sunny Paths and joy</span>
  </div>

  <p class="back-web">www.sunnypathsjoy.example</p>

  <footer class="social-band">
    <span class="social-item"><span class="social-dot"></span>@sunnypjoy</span>
    <span class="social-sep">|</span>
    <span class="social-item"><span class="social-dot"></span>sunnypathsandjoy.blogsite.example</span>
    <span class="social-sep">|</span>
    <span class="social-item"><span class="social-dot"></span>SunnyPathsAndJoy</span>
  </footer>
</section>

</body>
</html>
```